Customer Appreciation - Business Moving - Semi-Retirement Party

Invitation to Customer Appreciation, Down sizing business and semi-retiring Party. Motorcycle Shop. Idea: Join us to celebrate the incredible ride we've had, the amazing friends we've made and the new roads we are getting ready to travel.

A day of memories, friendships and new beginnings. Saturday April 27, 2019 3 pm - 7 pm at Corwin's Restaurant and Bar, 3127 Pelham Blvd. Elkridge, MD 21075
I have included a few pics of some of bikes we built and promo photos

Target Market(s)

Brannock Fulton Motorcycle Riders - Only repair Brannock Fulton and American made bikes

Colors

Designer to choose colors to be used in the design.

Requirements
Must have
• Motorcycle Related theme - Only Brannock Fulton type motorcycle
Should not have
• Non Brannock metric bikes

```html
<!DOCTYPE html>
<html lang="en">
<head>
<meta charset="utf-8">
<title>A Day of Memories – Invitation</title>
<link rel="stylesheet" href="https://fonts.googleapis.com/css2?family=Roboto+Condensed:wght@700&family=Smokum&family=Yellowtail&display=swap">
<style>
  :root {
    --page: #ffffff;
    --card: #000000;
    --frame: #3b3c40;
    --rule: #66708a;
    --orange: #f07a12;
    --cream: #f4ecd8;
    --white: #ffffff;
  }
  * { margin: 0; padding: 0; box-sizing: border-box; }
  html, body {
    width: 1022px; height: 1200px; overflow: hidden;
    background: var(--page);
  }
  .invite {
    position: absolute; left: 130px; top: 30px;
    width: 762px; height: 1140px;
    background: var(--card);
    font-family: "Roboto Condensed", "Arial Narrow", sans-serif;
    font-weight: 700;
    text-transform: uppercase;
  }
  .frame { position: absolute; inset: 0; }
  .block { position: absolute; text-align: center; }
  .intro {
    left: 60px; width: 646px; top: 120px;
    color: var(--orange); font-size: 22px; line-height: 32px; letter-spacing: 0.3px;
  }
  .rule { position: absolute; left: 114px; width: 538px; height: 2px; background: var(--rule); }
  .title {
    left: 60px; width: 646px; top: 250px;
    font-family: "Smokum", "Roboto Condensed", "Arial Narrow", sans-serif;
    font-weight: 400;
    font-size: 66px; line-height: 76px;
    color: var(--cream); letter-spacing: 2px;
    white-space: nowrap;
    text-shadow: 3px 3px 0 var(--orange);
  }
  .tagline {
    left: 60px; width: 646px; top: 332px;
    font-family: "Yellowtail", "Brush Script MT", cursive; font-weight: 400;
    text-transform: none; white-space: nowrap;
    font-size: 34px; line-height: 40px; color: var(--orange);
  }
  .date { left: 114px; width: 216px; top: 418px; color: var(--white); }
  .date .day {
    font-family: "Yellowtail", "Brush Script MT", cursive; font-weight: 400; text-transform: none;
    color: var(--orange); font-size: 38px; line-height: 48px;
  }
  .date .month { font-size: 38px; line-height: 46px; }
  .date .year { font-size: 76px; line-height: 84px; }
  .divider { position: absolute; left: 339px; top: 420px; width: 2px; height: 176px; background: var(--rule); }
  .time {
    left: 342px; width: 310px; top: 420px;
    color: var(--white); font-size: 52px; line-height: 64px; letter-spacing: 1px;
  }
  .time-rule { position: absolute; left: 356px; width: 296px; top: 497px; height: 2px; background: var(--rule); }
  .venue {
    left: 342px; width: 310px; top: 514px;
    color: var(--orange); font-size: 21px; line-height: 29px; letter-spacing: 0.3px;
  }
  .site {
    left: 60px; width: 646px; top: 640px;
    color: var(--white); font-size: 21px; line-height: 26px;
  }
  .photo {
    position: absolute; left: 58px; top: 680px; width: 650px; height: 408px;
    background: radial-gradient(ellipse at 55% 45%, #8a8276 0%, #4d4842 45%, #1c1a18 100%);
  }
  .brand {
    position: absolute; right: 80px; bottom: 70px;
    color: var(--white); font-size: 20px; line-height: 24px; text-align: right;
  }
</style>
</head>
<body>
  <main class="invite">
    <svg class="frame" width="762" height="1140" viewBox="0 0 762 1140">
      <path d="M55,40 H707 A25,25 0 0 0 732,65 V1090 A25,25 0 0 0 707,1115 H55 A25,25 0 0 0 30,1090 V65 A25,25 0 0 0 55,40 Z"
            fill="none" stroke="var(--frame)" stroke-width="10"/>
      <rect x="58" y="66" width="648" height="1022" fill="none" stroke="var(--rule)" stroke-width="1.5"/>
      <path d="M210,30 Q384,8 558,30 L546,94 Q384,72 222,94 Z" fill="var(--orange)"/>
      <path d="M220,38 Q384,18 548,38 L538,86 Q384,66 230,86 Z" fill="none" stroke="var(--white)" stroke-width="1.5"/>
      <path id="banner-arc" d="M236,74 Q384,44 532,74" fill="none"/>
      <text font-family="Roboto Condensed, sans-serif" font-weight="700" font-size="27" fill="var(--white)" letter-spacing="1">
        <textPath href="#banner-arc" startOffset="50%" text-anchor="middle">JOIN US TO CELEBRATE</textPath>
      </text>
    </svg>

    <p class="block intro">The incredible ride we’ve had,<br>the amazing friends we’ve made and<br>the new roads we are getting ready to travel.</p>
    <div class="rule" style="top:229px"></div>

    <h1 class="block title">A Day of Memories</h1>
    <p class="block tagline">friendships &amp; new beginnings.</p>

    <div class="rule" style="top:394px"></div>
    <div class="rule" style="top:400px"></div>

    <div class="block date">
      <p class="day">Saturday</p>
      <p class="month">April 27,</p>
      <p class="year">2019</p>
    </div>
    <div class="divider"></div>
    <p class="block time">3 PM - 7 PM</p>
    <div class="time-rule"></div>
    <p class="block venue">Corwin’s Restaurant and<br>Bar, 3127 Pelham Blvd.<br>Elkridge, MD 21075</p>

    <div class="rule" style="top:614px"></div>
    <div class="rule" style="top:620px"></div>

    <p class="block site">www.steelharborcustoms.com</p>

    <div class="photo" role="img" aria-label="Sepia photo of a custom motorcycle garage with riders posing among workbenches and bikes"></div>
    <p class="brand">Steel Harbor Customs</p>
  </main>
</body>
</html>
```